Social Media Marketing company needs a logo (tweak) and business card design

We need to slightly tidy up our logo, mainly to make sure we have the right design file (AI file type) also if possible remove the text below, for the business card we would like to get a fun yet professional feeling since we focus on social media marketing as well as event management
Target Market(s)
All industry really, just trying to look fun and professional to every one.
Industry/Entity Type
Marketing
Contact Information for Business Card
The Business Card needed to be fun yet professional
Font styles to use
Sans Serif
Colors
85cae6
Requirements
Must have
- The Logo.
- On the Name area, please provide two spaces 1. for English and Chinese.
- Rest is English only.
- Do not include a post code space.
- Phone number.
- Also please add website address www.brellavo.com
Nice to have
- Some water marks would be nice.
- Also the slogan "bright moves every day"

```html
<!DOCTYPE html>
<html lang="en">
<head>
<meta charset="utf-8">
<title>Brellavo — Business Card</title>
<link rel="stylesheet" href="https://fonts.googleapis.com/css2?family=Quicksand:wght@500;600;700&family=Montserrat:wght@700&family=Noto+Serif+SC:wght@300&display=swap">
<style>
  :root {
    --sky: #85cae6;
    --sky-soft: #7cc3e1;
    --ocean: #2f9fd6;
    --ink-blue: #2a95cf;
    --paper: #ffffff;
    --backdrop: #2c2c2c;
  }
  * { margin: 0; padding: 0; box-sizing: border-box; }
  html, body { width: 1189px; height: 1200px; overflow: hidden; }
  body {
    background: var(--backdrop);
    position: relative;
    font-family: "Quicksand", sans-serif;
  }
  .card {
    position: absolute;
    left: 171px;
    width: 856px;
    height: 487px;
    border-radius: 26px;
    overflow: hidden;
  }
  .card--front { top: 68px; background: var(--sky); }
  .card--back { top: 627px; background: var(--paper); }

  .front__watermark {
    position: absolute;
    inset: 0;
    background: radial-gradient(ellipse at 60% 45%, var(--sky-soft) 0%, var(--sky) 70%);
  }
  .front__mark {
    position: absolute;
    left: 358px;
    top: 142px;
    width: 140px;
    height: 140px;
    border-radius: 14px;
    background: var(--paper);
  }
  .front__brand {
    position: absolute;
    left: 0; right: 0;
    top: 400px;
    text-align: center;
    color: var(--paper);
    font-weight: 600;
    font-size: 58px;
    line-height: 1;
    letter-spacing: 0.5px;
  }

  .back__mark {
    position: absolute;
    left: 143px;
    top: 120px;
    width: 112px;
    height: 112px;
    border-radius: 12px;
    background: var(--sky);
  }
  .back__brand {
    position: absolute;
    left: 40px;
    width: 320px;
    top: 268px;
    text-align: center;
    color: var(--ink-blue);
    font-weight: 600;
    font-size: 44px;
    line-height: 1;
  }
  .back__slogan {
    position: absolute;
    left: 40px;
    width: 320px;
    top: 324px;
    text-align: center;
    color: var(--ink-blue);
    font-weight: 500;
    font-size: 15px;
    letter-spacing: 3.2px;
  }
  .back__divider {
    position: absolute;
    left: 408px;
    top: 79px;
    width: 2px;
    height: 269px;
    background: var(--ocean);
  }
  .person { position: absolute; left: 455px; top: 82px; }
  .person__name {
    font-family: "Montserrat", sans-serif;
    font-weight: 700;
    font-size: 30px;
    line-height: 34px;
    color: var(--ink-blue);
  }
  .person__name-zh {
    font-family: "Noto Serif SC", serif;
    font-weight: 300;
    font-size: 23px;
    line-height: 28px;
    color: var(--sky);
  }
  .person__role {
    font-size: 21px;
    line-height: 30px;
    color: var(--sky);
    font-weight: 500;
  }
  .contact { position: absolute; left: 455px; top: 256px; list-style: none; }
  .contact__item {
    display: flex;
    align-items: center;
    gap: 9px;
    height: 30px;
    font-size: 22px;
    font-weight: 500;
    color: var(--ocean);
  }
  .contact__icon { width: 27px; height: 26px; flex: none; }
  .back__wave { position: absolute; left: 0; top: 0; width: 856px; height: 487px; }
</style>
</head>
<body>
  <section class="card card--front">
    <div class="front__watermark" role="img" aria-label="Faint circuit-line watermark pattern in a slightly deeper blue"></div>
    <div class="front__mark" aria-hidden="true"></div>
    <p class="front__brand">Brellavo</p>
  </section>

  <section class="card card--back">
    <svg class="back__wave" viewBox="0 0 856 487" aria-hidden="true">
      <path d="M0 392 C 230 492, 520 448, 856 378 V487 H0 Z" fill="var(--sky)"/>
      <path d="M4 377 C 230 478, 520 440, 846 366 C 520 428, 240 464, 4 377 Z" fill="var(--ocean)"/>
    </svg>

    <div class="back__mark" aria-hidden="true"></div>
    <p class="back__brand">Brellavo</p>
    <p class="back__slogan">bright moves every day</p>

    <div class="back__divider"></div>

    <div class="person">
      <p class="person__name">DANIEL REEVE</p>
      <p class="person__name-zh">丹尼尔 · 里夫</p>
      <p class="person__role">Maneger</p>
    </div>

    <ul class="contact">
      <li class="contact__item">
        <svg class="contact__icon" viewBox="0 0 27 26" aria-hidden="true">
          <rect width="27" height="26" rx="3" fill="var(--sky)"/>
          <path d="M10 6 l3 0 l1 4 l-2 1.5 c1 2.5 2 3.5 3.5 4.5 l1.5-2 l4 1 l0 3 c-7 0-11-5-11-12z" fill="#fff"/>
        </svg>
        <span>5550142287</span>
      </li>
      <li class="contact__item">
        <svg class="contact__icon" viewBox="0 0 27 26" aria-hidden="true">
          <rect width="27" height="26" rx="3" fill="var(--sky)"/>
          <rect x="5" y="7.5" width="17" height="11" fill="none" stroke="#fff" stroke-width="1.6"/>
          <path d="M5 7.5 L13.5 14 L22 7.5" fill="none" stroke="#fff" stroke-width="1.6"/>
        </svg>
        <span>hello@brellavo.com</span>
      </li>
      <li class="contact__item">
        <svg class="contact__icon" viewBox="0 0 27 26" aria-hidden="true">
          <rect width="27" height="26" rx="3" fill="var(--sky)"/>
          <circle cx="13.5" cy="13" r="7.5" fill="none" stroke="#fff" stroke-width="1.6"/>
          <path d="M6 13 H21 M13.5 5.5 C10 9, 10 17, 13.5 20.5 M13.5 5.5 C17 9, 17 17, 13.5 20.5" fill="none" stroke="#fff" stroke-width="1.4"/>
        </svg>
        <span>www.brellavo.com</span>
      </li>
    </ul>
  </section>
</body>
</html>
```